Web Design Project

The client is unsure if they want a completely new design or a design that matches their existing site closely (https://www.kelvatcover.com.au). So essentially we are looking for some designs that reflect the existing sites shape and colour and some designs that have their own new style. The company will sell three main types of insurance, Car, Bike and Caravan.

Read the complete brief and in the attached document.
The logo is also attached

I have also attached a zip of a few classic cars, if you can incorporate those.

Industry/Entity Type

Insurance

Requirements
Should not have
• Print This Page
Site Search

```html
<!DOCTYPE html>
<html lang="en">
<head>
<meta charset="utf-8">
<title>Kelvat Cover – Classic &amp; Prestige Vehicle Insurance</title>
<link rel="stylesheet" href="https://fonts.googleapis.com/css2?family=Arimo:wght@400;700&family=Roboto:wght@700&display=swap">
<style>
:root{
  --page:#f1f1f1;
  --white:#ffffff;
  --ink:#333333;
  --muted:#6a6a6a;
  --accent:#e0622a;
  --red:#d6372a;
  --red-dark:#b9261d;
  --nav-top:#555555;
  --nav-bottom:#2c2c2c;
  --panel:#f5f5f5;
  --line:#dddddd;
}
*{margin:0;padding:0;box-sizing:border-box}
html,body{width:952px;height:1200px;overflow:hidden}
body{background:var(--page);font-family:"Arimo",Arial,sans-serif;color:var(--ink);position:relative}
.abs{position:absolute}
ul,li{list-style:none}

/* top strip */
.hotline{left:405px;top:18px;font-size:13px;color:#444;display:flex;align-items:center;gap:6px}
.hotline strong{font-family:"Roboto",Arial,sans-serif;font-weight:700;font-size:20px;color:var(--red);margin-left:6px}
.search{left:718px;top:15px;width:164px;height:22px;background:var(--white);border:1px solid #d2d2d2;font-size:9px;color:#888;padding:5px 11px}
.search svg{position:absolute;right:6px;top:4px}

/* navigation */
.navbar{left:70px;top:55px;width:812px;height:53px;background:linear-gradient(var(--nav-top),var(--nav-bottom));box-shadow:0 6px 10px rgba(0,0,0,.12)}
.brand{left:74px;top:56px;width:166px;height:52px;display:flex;align-items:center;justify-content:center;gap:7px;color:var(--white);font-size:13px;letter-spacing:1px}
.brand i{width:9px;height:9px;border-radius:50%;background:var(--white);display:block}
.menu{left:262px;top:55px;display:flex;height:53px}
.menu a{color:var(--white);text-decoration:none;font-size:12px;display:flex;align-items:center;justify-content:center;border-left:1px solid #222;box-shadow:inset 1px 0 #5c5c5c;height:53px}
.menu a.active{background:linear-gradient(#e0552d,var(--red-dark))}
.dropdown{left:330px;top:108px;width:141px;height:118px;background:linear-gradient(var(--red),var(--red-dark));border:1px solid #e86a4d;padding:8px 0 0 14px;z-index:20;box-shadow:0 3px 6px rgba(0,0,0,.2)}
.dropdown li{color:var(--white);font-size:11.5px;height:25px;display:flex;align-items:center;gap:10px;white-space:nowrap}
.dropdown li::before{content:"";flex:none;width:4px;height:4px;border-radius:50%;background:#5a1410}
.account{left:105px;top:121px;font-size:11px;color:#333}
.account span{margin:0 8px;color:#888}

/* slider */
.slide{top:141px;width:257px;height:302px;background:var(--white);padding:5px;box-shadow:0 1px 3px rgba(0,0,0,.15)}
.slide .pic{width:100%;height:100%;position:relative;overflow:hidden}
.slide.car .pic{background:linear-gradient(160deg,#5a5a5a,#8a8a8a 45%,#3a3a3a)}
.slide.bike .pic{background:linear-gradient(170deg,#7fa4c6 0%,#6f8f5e 35%,#5d5f5c 60%,#2e2e2e 100%)}
.slide.van .pic{background:linear-gradient(180deg,#1f5fc4 0%,#5c9ae0 40%,#d8d8d8 70%,#f2f2f2 100%)}
.car-text{position:absolute;inset:0;background:rgba(40,40,40,.7);padding:30px 20px 0 20px;color:var(--white)}
.car-text h2{font-family:"Roboto",Arial,sans-serif;font-weight:700;font-size:20px;padding-bottom:13px;border-bottom:1px solid #999}
.car-text p{font-size:10.5px;line-height:18.2px;text-align:justify;padding:11px 0 13px;border-bottom:1px solid #999}
.caption{position:absolute;left:0;right:0;bottom:0;height:45px;background:rgba(20,20,20,.55);color:var(--white);font-family:"Roboto",Arial,sans-serif;font-weight:700;font-size:20px;display:flex;align-items:center;justify-content:center}
.reflection{top:449px;width:257px;height:30px;background:linear-gradient(rgba(255,255,255,.7),rgba(241,241,241,0))}
.arrow{top:273px;width:34px;height:34px;border-radius:50%;background:var(--white);box-shadow:0 1px 4px rgba(0,0,0,.25);display:flex;align-items:center;justify-content:center}

/* quote tab */
.quote-label{left:870px;top:472px;width:65px;text-align:right;font-size:10px;line-height:15px;color:#999}
.quote-tab{left:882px;width:46px;height:51px;border-radius:0 5px 5px 0;display:flex;align-items:center;justify-content:center}
.quote-tab.dark{top:505px;background:linear-gradient(#555,#2c2c2c)}
.quote-tab.light{top:565px;background:linear-gradient(#bbb,#888)}

/* intro */
.intro{left:70px;top:491px;width:812px;height:134px;background:linear-gradient(var(--white),#fafafa);text-align:center;padding-top:20px}
.intro h1{font-weight:400;font-size:22px;color:var(--accent)}
.intro p{font-size:10.6px;line-height:18.3px;color:var(--muted);width:710px;margin:10px auto 0}

/* main area */
.main{left:70px;top:637px;width:812px;height:481px;background:var(--white)}
.section-title{font-weight:400;font-size:18.5px;color:var(--accent)}
.benefits{left:81px;top:692px;width:569px;height:274px;border-radius:6px;background:linear-gradient(100deg,#f6f6f6 40%,#ececec);overflow:hidden}
.benefits .art{position:absolute;right:0;bottom:0;width:340px;height:190px;background:radial-gradient(ellipse at 70% 60%,#e3e3e3,rgba(246,246,246,0) 70%)}
.benefits ul{position:absolute;left:21px;top:8px}
.benefits li{font-size:11px;height:26.5px;display:flex;align-items:center;gap:14px}
.partners{left:83px;top:1042px;display:flex;gap:10px;align-items:center}
.partners span{display:block;height:34px;border-radius:3px}

/* sidebar */
.widget-head{left:664px;width:209px;height:47px;background:linear-gradient(#555,#2e2e2e);color:var(--white);font-size:18.5px;display:flex;align-items:center;padding-left:66px;border-radius:3px 3px 0 0}
.widget-head .icon{position:absolute;left:20px;top:11px}
.news{left:664px;top:697px;width:209px;height:240px;background:#f7f7f7;border:1px solid #e4e4e4;border-top:0}
.news article{padding:14px 9px 0 15px;height:118px;border-bottom:1px solid #e3e3e3}
.news time{font-size:10.5px;color:#222;display:block;margin-bottom:8px}
.news p{font-size:10.5px;line-height:15px;color:var(--muted);text-align:justify}
.more{font-size:10.5px;color:var(--accent);margin-top:5px;display:block}
.more::before{content:"› ";font-size:9px}
.view-all{left:664px;width:209px;height:30px;background:#ececec;border:1px solid #e0e0e0;font-size:11px;color:var(--accent);display:flex;align-items:center;justify-content:center}
.view-all::before{content:"› ";font-size:9px;margin-right:3px}
.events{left:664px;top:1018px;width:209px;height:68px;background:#f7f7f7;border:1px solid #e4e4e4;border-top:0}
.event-banner{position:absolute;left:19px;top:15px;width:171px;height:33px;background:linear-gradient(90deg,#d5261e 0 40%,#1f8ee0 40%)}

/* footer */
.foot-links{left:70px;top:1141px;font-size:10.5px;color:#555}
.foot-links span{margin:0 5px;color:#999}
.copyright{left:70px;top:1167px;font-size:10px;color:#555}
.social{top:1151px;width:19px;height:19px;border-radius:2px}
</style>
</head>
<body>

<div class="abs hotline">
  <svg width="18" height="14" viewBox="0 0 18 14"><path d="M2 4c3-4 11-4 14 0l-2 2-3-1V3H7v2L4 6z" fill="#555" transform="rotate(15 9 7)"/></svg>
  Insure with an Enthusiast <strong>1300 555 218</strong>
</div>
<div class="abs search">Search
  <svg width="13" height="13" viewBox="0 0 13 13"><circle cx="5" cy="5" r="3.6" fill="none" stroke="#222" stroke-width="1.8"/><path d="M7.7 7.7l4 4" stroke="#222" stroke-width="2.2"/></svg>
</div>

<div class="abs navbar"></div>
<div class="abs brand"><i></i>KELVAT COVER</div>
<nav class="abs menu">
  <a style="width:68px">HOME</a>
  <a class="active" style="width:88px">ABOUT US</a>
  <a style="width:100px">INSURANCE</a>
  <a style="width:75px">EVENTS</a>
  <a style="width:66px">CLUBS</a>
  <a style="width:63px">LINKS</a>
  <a style="width:55px">FAQ</a>
  <a style="width:106px">CONTACT US</a>
</nav>
<div class="abs account">LOGIN<span>|</span>REGISTER</div>

<div class="abs slide car" style="left:84px">
  <div class="pic" role="img" aria-label="Driver beside a classic car">
    <div class="car-text">
      <h2>Car Insurance</h2>
      <p>Suspendisse potenti. Suspendisse nec orci tellus, nec cursus dui. In lectus leo, porta quis ultrices a, tristique nec enim. Sed luctus blandit eros, vitae interdum quam venenatis quis. Proin sollicitudin, leo in laoreet posuere, sem neque varius neque, a sagittis arcu libero in est. Suspendisse nec dui vel ante egestas</p>
    </div>
  </div>
</div>
<div class="abs slide bike" style="left:349px">
  <div class="pic" role="img" aria-label="Rider on a motorcycle along a tree-lined road"><div class="caption">Bike Insurance</div></div>
</div>
<div class="abs slide van" style="left:616px">
  <div class="pic" role="img" aria-label="Vintage caravan under a blue sky"><div class="caption">Caravan Insurance</div></div>
</div>
<div class="abs reflection" style="left:84px"></div>
<div class="abs reflection" style="left:349px"></div>
<div class="abs reflection" style="left:616px"></div>
<div class="abs arrow" style="left:70px"><svg width="10" height="14"><path d="M8 1L2 7l6 6" fill="none" stroke="#777" stroke-width="1.5"/></svg></div>
<div class="abs arrow" style="left:847px"><svg width="10" height="14"><path d="M2 1l6 6-6 6" fill="none" stroke="#777" stroke-width="1.5"/></svg></div>

<ul class="abs dropdown">
  <li>Dropdown Menu 1</li><li>Dropdown Menu 2</li><li>Dropdown Menu 3</li><li>Dropdown Menu 4</li>
</ul>

<div class="abs quote-label">Request<br>a Quote</div>
<div class="abs quote-tab dark"><svg width="22" height="24"><rect x="3" y="2" width="15" height="19" fill="#f4f4f4" transform="rotate(-12 10 12)"/><path d="M7 9h8M7 12h8M7 15h6" stroke="#999" stroke-width="1"/></svg></div>
<div class="abs quote-tab light"><svg width="30" height="14"><path d="M2 10l3-4h7l4-3h6l5 4 2 3z" fill="#1d4fbf"/><circle cx="8" cy="11" r="2" fill="#222"/><circle cx="22" cy="11" r="2" fill="#222"/></svg></div>

<section class="abs intro">
  <h1>The specialised car insurance cover your Classic or Prestige car needs</h1>
  <p>Kelvat Cover shares your passion for classic cars, vintage cars, prestige cars and hot rods.&nbsp; Don't just trust your specialist vehicle insurance to a general insurance provider – we're specialists, we've only insured cars like yours and will cover your car like it's one of our own. Call today to find out how much more we can do for you.</p>
</section>

<div class="abs main"></div>
<h2 class="abs section-title" style="left:81px;top:663px">Our Policy Benefits</h2>
<div class="abs benefits">
  <div class="art" role="img" aria-label="Faint classic sports cars"></div>
  <ul>
    <li><svg width="10" height="10"><circle cx="5" cy="5" r="4.3" fill="none" stroke="#777"/><path d="M3 5l1.6 1.6L7.2 3.6" fill="none" stroke="#555" stroke-width="1.2"/></svg>Agreed Value</li>
    <li><svg width="10" height="10"><circle cx="5" cy="5" r="4.3" fill="none" stroke="#777"/><path d="M3 5l1.6 1.6L7.2 3.6" fill="none" stroke="#555" stroke-width="1.2"/></svg>New Replacement Vehicle in first 2 years</li>
    <li><svg width="10" height="10"><circle cx="5" cy="5" r="4.3" fill="none" stroke="#777"/><path d="M3 5l1.6 1.6L7.2 3.6" fill="none" stroke="#555" stroke-width="1.2"/></svg>Choice of Repairer</li>
    <li><svg width="10" height="10"><circle cx="5" cy="5" r="4.3" fill="none" stroke="#777"/><path d="M3 5l1.6 1.6L7.2 3.6" fill="none" stroke="#555" stroke-width="1.2"/></svg>Lifetime Guarantee for Repairs</li>
    <li><svg width="10" height="10"><circle cx="5" cy="5" r="4.3" fill="none" stroke="#777"/><path d="M3 5l1.6 1.6L7.2 3.6" fill="none" stroke="#555" stroke-width="1.2"/></svg>Free Windscreen/Glass Benefit</li>
    <li><svg width="10" height="10"><circle cx="5" cy="5" r="4.3" fill="none" stroke="#777"/><path d="M3 5l1.6 1.6L7.2 3.6" fill="none" stroke="#555" stroke-width="1.2"/></svg>Hire car following accident or theft</li>
    <li><svg width="10" height="10"><circle cx="5" cy="5" r="4.3" fill="none" stroke="#777"/><path d="M3 5l1.6 1.6L7.2 3.6" fill="none" stroke="#555" stroke-width="1.2"/></svg>Flexible coverage</li>
    <li><svg width="10" height="10"><circle cx="5" cy="5" r="4.3" fill="none" stroke="#777"/><path d="M3 5l1.6 1.6L7.2 3.6" fill="none" stroke="#555" stroke-width="1.2"/></svg>Pay Premiums by Instalments</li>
    <li><svg width="10" height="10"><circle cx="5" cy="5" r="4.3" fill="none" stroke="#777"/><path d="M3 5l1.6 1.6L7.2 3.6" fill="none" stroke="#555" stroke-width="1.2"/></svg>Salvage retained by you on</li>
    <li><svg width="10" height="10"><circle cx="5" cy="5" r="4.3" fill="none" stroke="#777"/><path d="M3 5l1.6 1.6L7.2 3.6" fill="none" stroke="#555" stroke-width="1.2"/></svg>vehicles over 30 years</li>
  </ul>
</div>

<h2 class="abs section-title" style="left:81px;top:1001px">Affiliations</h2>
<div class="abs partners" aria-label="Partner badges">
  <span style="width:97px;background:#f2c200"></span>
  <span style="width:100px;background:#e8e8e8"></span>
  <span style="width:93px;height:16px;background:#333"></span>
  <span style="width:65px;background:#f4d5d5;border:2px solid #c8242a"></span>
  <span style="width:93px;height:28px;background:#222"></span>
  <span style="width:60px;background:#f3e3e3"></span>
</div>

<div class="abs widget-head" style="top:650px">
  <svg class="icon" width="36" height="26"><rect x="3" y="5" width="28" height="17" rx="2" fill="#ddd" transform="rotate(-12 17 13)"/><path d="M9 10h16M9 14h16" stroke="#888" transform="rotate(-12 17 13)"/></svg>
  Latest News
</div>
<div class="abs news">
  <article>
    <time>March-04-2013</time>
    <p>In almost 50i years, the expectations were high on the latest offering from the Vantor sportscar. It has taken almost 50 years,</p>
    <span class="more">more</span>
  </article>
  <article>
    <time>March-04-2013</time>
    <p>In almost 50i years, the expectations were high on the latest offering from the Vantor sportscar. It has taken almost 50 years,</p>
    <span class="more">more</span>
  </article>
</div>
<div class="abs view-all" style="top:937px">VIEW ALL</div>

<div class="abs widget-head" style="top:971px">
  <svg class="icon" width="30" height="28"><rect x="3" y="4" width="24" height="22" rx="2" fill="#eee"/><rect x="3" y="4" width="24" height="6" fill="#e0622a"/><path d="M7 14h16M7 18h16M7 22h16" stroke="#bbb"/></svg>
  Latest Events
</div>
<div class="abs events">
  <div class="event-banner" role="img" aria-label="Annual swap meet and car show banner"></div>
</div>
<div class="abs view-all" style="top:1085px">VIEW ALL</div>

<div class="abs foot-links">Home<span>|</span>About us<span>|</span>Insurance<span>|</span>Events<span>|</span>Clubs<span>|</span>Links<span>|</span>FAQ<span>|</span>Contact us</div>
<div class="abs copyright">Copyright &nbsp;© &nbsp;2013 &nbsp;&nbsp;www.kelvatcover.com.au &nbsp;&nbsp;&nbsp;All rights reserved.</div>
<div class="abs social" style="left:838px;background:#3b5998"></div>
<div class="abs social" style="left:863px;background:#3fb2e6"></div>

</body>
</html>
```